Food Trade Show Advertisement

One full-page advertisement sent as a high-resolution .pdf file that is 11.125" w x 14.25" h

Details on the the wording and pictures will be provided
The to include:
Company logo, product photos (to be supplied), wording (to be supplied), Booth number (to be supplied)
Colors - hot pink
Attached is the guidelines for the advertisement

```html
<!DOCTYPE html>
<html lang="en">
<head>
<meta charset="utf-8">
<title>All Purpose Flour &amp; TVP – Trade Show Advertisement</title>
<link rel="stylesheet" href="https://fonts.googleapis.com/css2?family=Archivo:wght@600;700;800;900&family=Roboto+Condensed:wght@700&display=swap">
<style>
  :root {
    --hot-pink: #ec1384;
    --tan: #a88a5c;
    --outline-beige: #eadfcc;
    --lime: #2cf22c;
    --white: #ffffff;
    --sack-grey: #9d9c9f;
    --flour-cream: #ecd9a8;
    --tvp-gold: #dcb774;
    --leaf-green: #22d622;
  }
  * { margin: 0; padding: 0; box-sizing: border-box; }
  html, body { width: 1000px; height: 1200px; overflow: hidden; background: var(--white); }
  .ad {
    position: relative;
    width: 1000px;
    height: 1200px;
    background: var(--white);
    overflow: hidden;
    font-family: "Archivo", Arial, sans-serif;
  }
  .corner-shape { position: absolute; left: 0; top: 0; }
  .backdrop-word {
    position: absolute;
    left: 450px;
    top: -30px;
    font-weight: 800;
    font-size: 180px;
    letter-spacing: 2px;
    color: transparent;
    -webkit-text-stroke: 3px var(--outline-beige);
    white-space: nowrap;
  }
  .photo { position: absolute; }
  .photo--flour-pile {
    left: 500px; top: 60px; width: 430px; height: 530px;
    border-radius: 48% 40% 46% 42%;
    background: radial-gradient(ellipse at 50% 50%, var(--flour-cream) 0%, #f2e4c2 65%, rgba(242,228,194,0) 100%);
  }
  .photo--sack {
    left: 60px; top: 46px; width: 580px; height: 452px;
    border-radius: 30px 60px 40px 24px;
    background: linear-gradient(160deg, #b0afb2 0%, var(--sack-grey) 55%, #8a898c 100%);
    box-shadow: 0 24px 40px rgba(0,0,0,0.18);
  }
  .photo--tvp {
    left: 430px; top: 740px; width: 490px; height: 268px;
    border-radius: 50% 50% 40% 40% / 70% 70% 30% 30%;
    background: radial-gradient(ellipse at 50% 60%, var(--tvp-gold) 0%, #e6c98f 60%, rgba(240,220,180,0) 100%);
  }
  .headline-lead {
    position: absolute; left: 54px; top: 556px;
    color: var(--tan); font-weight: 800; line-height: 1; white-space: nowrap;
  }
  .headline-lead .line-1 { display: block; font-size: 38px; letter-spacing: -0.8px; }
  .headline-lead .line-2 { display: block; font-size: 53px; margin-top: 8px; letter-spacing: -0.8px; }
  .headline-product {
    position: absolute; left: 488px; top: 540px;
    color: var(--hot-pink); font-weight: 900; font-size: 122px; line-height: 1; letter-spacing: -3px;
    white-space: nowrap;
  }
  .sub-lead {
    position: absolute; left: 60px; top: 688px;
    color: var(--tan); font-weight: 700; font-size: 40px; letter-spacing: -0.5px; white-space: nowrap;
  }
  .tvp-mark {
    position: absolute; left: 56px; top: 748px;
    color: var(--hot-pink); font-weight: 900; font-size: 168px; line-height: 1; letter-spacing: -4px;
    text-shadow: -4px -3px 0 var(--lime);
  }
  .quality {
    position: absolute; left: 72px; top: 930px; width: 330px;
    border-top: 2px solid var(--hot-pink);
    border-bottom: 2px solid var(--hot-pink);
    padding: 4px 0 2px;
    font-family: "Roboto Condensed", "Arial Narrow", sans-serif;
    font-weight: 700; font-size: 44px; line-height: 1.05; color: var(--tan); white-space: nowrap;
  }
  .website {
    position: absolute; left: 78px; top: 1004px;
    display: flex; align-items: center; gap: 14px;
    color: var(--tan); font-weight: 700; font-size: 31px; white-space: nowrap;
  }
  .booth-band {
    position: absolute; left: 0; top: 1048px; width: 516px; height: 109px;
    background: var(--hot-pink);
    border-radius: 0 56px 56px 0;
    display: flex; align-items: center; padding-left: 50px;
    color: var(--white); font-weight: 800; font-size: 64px; letter-spacing: -1px;
    white-space: nowrap;
  }
  .brand {
    position: absolute; top: 1060px; height: 100px;
    display: flex; align-items: center; gap: 8px;
    font-weight: 800; white-space: nowrap;
  }
  .brand--meadowfield { left: 556px; font-size: 18px; letter-spacing: 2px; color: var(--leaf-green); }
  .brand--meadowfield .dot { width: 12px; height: 12px; border-radius: 50%; background: var(--leaf-green); }
  .brand--bellaro { left: 790px; font-size: 44px; color: var(--hot-pink); }
</style>
</head>
<body>
  <main class="ad">
    <svg class="corner-shape" width="420" height="572" viewBox="0 0 420 572" aria-hidden="true">
      <path d="M0 0 H418 C 400 230, 230 470, 0 570 Z" fill="var(--hot-pink)"/>
    </svg>

    <div class="backdrop-word" aria-hidden="true">FLOUR</div>

    <div class="photo photo--flour-pile" role="img" aria-label="Pile of all purpose flour spilling out of a sack"></div>
    <div class="photo photo--sack" role="img" aria-label="Grey cloth flour sack lying on its side"></div>

    <h1 class="headline-lead">
      <span class="line-1">WE ARE PROVIDING</span>
      <span class="line-2">ALL PURPOSE</span>
    </h1>
    <div class="headline-product">FLOUR</div>

    <p class="sub-lead">We are also supply</p>
    <div class="tvp-mark">TVP</div>

    <div class="photo photo--tvp" role="img" aria-label="Heap of textured vegetable protein chunks with flexing arm doodles"></div>

    <p class="quality">in Export Quality</p>

    <p class="website">
      <svg width="28" height="28" viewBox="0 0 28 28" aria-hidden="true" fill="none" stroke="var(--tan)" stroke-width="2">
        <circle cx="14" cy="14" r="12"/>
        <ellipse cx="14" cy="14" rx="5.5" ry="12"/>
        <line x1="2" y1="14" x2="26" y2="14"/>
        <line x1="4.5" y1="8" x2="23.5" y2="8"/>
        <line x1="4.5" y1="20" x2="23.5" y2="20"/>
      </svg>
      www.grainlane.net
    </p>

    <div class="booth-band">BOOTH 1029</div>

    <div class="brand brand--meadowfield"><span class="dot"></span>MEADOWFIELD</div>
    <div class="brand brand--bellaro">Bellaro</div>
  </main>
</body>
</html>
```